Health Information/Education Logo Design

We need a logo design for a new company based in Atlanta called Brightpath Care. The program is about patient empowerment. We provide health information and education on how to get healthy, stay healthy, and how to be proactive in your care. We also provide medication and injection training to help patients feel their best and to ensure successful therapy outcomes.
We like the colors yellow, pink, teal and purple and would like to see some or all of these colors in the designs. The final design should communicate caring, considerate, compassionate information, education and training services
Education
Contact Information for Business Card
Brightpath Care
Lorraine Pettaway RN, MSN, MHA
Nurse Educator
404.555.0187 cell
404.555.0142 fax

```html
<!DOCTYPE html>
<html lang="en">
<head>
<meta charset="utf-8">
<title>Brightpath Care – Business Card</title>
<link href="https://fonts.googleapis.com/css2?family=Questrial&display=swap" rel="stylesheet">
<style>
  :root {
    --frame-purple: #461e5f;
    --cream-yellow: #fcf29c;
    --peach: #fde0c8;
    --blush: #fbd6e2;
    --wave-sand: #ecd0b0;
    --wave-mauve: #cf9fc6;
    --brand-teal: #1c9a78;
    --ink-green: #0f4a3b;
    --mark-lavender: #b497cf;
  }
  html, body {
    margin: 0;
    padding: 0;
    width: 1200px;
    height: 701px;
    overflow: hidden;
    background: var(--frame-purple);
  }
  .card {
    position: relative;
    width: 1200px;
    height: 701px;
    background: var(--frame-purple);
    font-family: "Questrial", sans-serif;
  }
  .card-face {
    position: absolute;
    left: 55px;
    top: 57px;
    width: 1091px;
    height: 588px;
    overflow: hidden;
  }
  .card-face svg {
    position: absolute;
    inset: 0;
  }
  .brand-dot {
    position: absolute;
    left: 80px;
    top: 70px;
    width: 230px;
    height: 230px;
    border-radius: 50%;
    background: var(--mark-lavender);
  }
  .brand-name {
    position: absolute;
    left: 300px;
    top: 58px;
    margin: 0;
    font-weight: 400;
    font-size: 92px;
    line-height: 98px;
    color: var(--brand-teal);
  }
  .brand-name span { display: block; }
  .contact {
    position: absolute;
    right: 20px;
    margin: 0;
    color: var(--ink-green);
    font-size: 45px;
    line-height: 1;
    white-space: nowrap;
    letter-spacing: 1.5px;
  }
  .contact-name { top: 346px; }
  .contact-title { top: 427px; }
  .contact-numbers { top: 497px; left: 14px; right: auto; }
</style>
</head>
<body>
  <div class="card">
    <div class="card-face">
      <svg width="1091" height="588" viewBox="0 0 1091 588" aria-hidden="true">
        <defs>
          <linearGradient id="face-bg" x1="0" y1="0" x2="1" y2="0">
            <stop offset="0" stop-color="var(--cream-yellow)"/>
            <stop offset="0.55" stop-color="var(--peach)"/>
            <stop offset="1" stop-color="var(--blush)"/>
          </linearGradient>
          <linearGradient id="wave-fill" x1="0" y1="0" x2="1" y2="0">
            <stop offset="0" stop-color="var(--wave-sand)"/>
            <stop offset="1" stop-color="var(--wave-mauve)"/>
          </linearGradient>
        </defs>
        <rect width="1091" height="588" fill="url(#face-bg)"/>
        <path class="lower-wave" d="M0 420 C 260 500, 520 470, 720 330 C 880 215, 1000 150, 1091 100 L1091 588 L0 588 Z" fill="url(#wave-fill)" opacity="0.9"/>
      </svg>
      <div class="brand-dot"></div>
      <h1 class="brand-name"><span>Brightpath</span><span>Care</span></h1>
      <p class="contact contact-name">Lorraine Pettaway</p>
      <p class="contact contact-title">RN, MSN, MHA Nurse Educator</p>
      <p class="contact contact-numbers">Cell:404.555.0187 Fax:404.555.0142</p>
    </div>
  </div>
</body>
</html>
```